Covid19 Poster for workplaces

Create a poster on how to protect yourself from Corona virus at work.
We are a Thrive at Work company. We have just re-branded so we need to fit in with our brand. We like clean and fresh, slightly amusing is ok if it will draw attention but it's an important topic. A4 and A3 please.

Content:

Headline: Lower the risk of COVID 19 in the workplace.

BE WELL

Bring your own cup - don’t share cups and food.
Elbow tap instead of handshakes and kisses
Wash your hands often - with soap.
Elbow or tissues when you cough or sneeze then straight in the bin
Leave your face alone after touching shared surfaces
Leave your bugs at home if you’re feeling unwell.

Call health line if you have a cough, a high temperature and shortness of breath. 0800 472 9160

Based on recommendations from ZPK and QLN

Target Market(s)

Employees - so anyone

Other font styles liked:
• Use the closest font to the brand documents

Requirements
Should not have
• Clip art

```html
<!DOCTYPE html>
<html lang="en">
<head>
<meta charset="utf-8">
<title>Lower the risk of COVID-19 in the workplace</title>
<link href="https://fonts.googleapis.com/css2?family=Poppins:wght@400;600;700;800&display=swap" rel="stylesheet">
<style>
:root{
  --stage:#4cefc2;
  --lime:#8cfc03;
  --ink:#1d1d1b;
  --paper:#ffffff;
  --alert:#f2647a;
  --photo-a:#9aa3a8;
  --photo-b:#5d6b72;
}
*{margin:0;padding:0;box-sizing:border-box}
html,body{width:1200px;height:1084px;overflow:hidden}
body{background:var(--stage);font-family:'Poppins',sans-serif;color:var(--ink);position:relative}
.poster{position:absolute;left:240px;top:33px;width:720px;height:1018px;background:var(--paper);overflow:hidden}
.header{position:absolute;left:0;top:0;width:720px;height:241px;background:var(--lime)}
.header-title{position:absolute;left:64px;top:38px;color:var(--paper);font-weight:800;font-size:46px;line-height:42px;letter-spacing:-0.5px}
.header-url{position:absolute;left:67px;top:194px;color:var(--paper);font-weight:600;font-size:13px}
.header-photo{position:absolute;left:326px;top:26px;width:351px;height:188px;border-radius:60px;background:linear-gradient(135deg,var(--photo-a),var(--photo-b))}
.headline{position:absolute;left:64px;top:278px;font-weight:800;font-size:44px;line-height:48px;letter-spacing:-0.5px}
.headline .accent{color:var(--lime);display:block}
.headline .plain{color:var(--ink);display:block}
.tips{position:absolute;left:64px;top:408px;width:400px;list-style:none}
.tip{position:relative;height:63.5px;border-bottom:1px solid var(--ink);padding-left:79px;padding-top:4px}
.tip:last-child{border-bottom:none}
.tip-icon{position:absolute;left:0;top:6px;width:48px;height:48px}
.tip-title{color:var(--lime);font-weight:700;font-size:22px;line-height:28px;white-space:nowrap}
.tip-text{font-size:11px;line-height:16px;white-space:nowrap}
.footer-shape{position:absolute;left:0;top:0;width:720px;height:1018px}
.helpline{position:absolute;left:70px;top:866px;color:var(--paper);font-weight:800;font-size:37px;line-height:44px}
.helpline-note{position:absolute;left:70px;top:910px;font-weight:700;font-size:15.5px;line-height:19px;width:340px}
.partners{position:absolute;left:70px;top:954px;display:flex;gap:14px;align-items:center}
.partner-circle{width:20px;height:20px;border-radius:50%;border:2px solid var(--paper)}
.partner-square{width:20px;height:16px;background:var(--paper);opacity:.9}
.source{position:absolute;left:70px;top:983px;color:var(--paper);font-size:9.5px}
.brand{position:absolute;left:515px;top:946px;display:flex;align-items:center;gap:10px}
.brand-dot{width:34px;height:34px;border-radius:50%;background:var(--lime)}
.brand-name{font-weight:700;font-size:19px;line-height:19px;color:var(--ink)}
</style>
</head>
<body>
<main class="poster">
  <header class="header">
    <h1 class="header-title">Wellbeing<br>matters at<br>work</h1>
    <p class="header-url">www.thriveatworkhq.co.nz</p>
    <div class="header-photo" role="img" aria-label="Photo of cheerful colleagues celebrating in an office"></div>
  </header>

  <h2 class="headline"><span class="accent">Lower the risk of COVID-19</span><span class="plain">in the workplace</span></h2>

  <ul class="tips">
    <li class="tip">
      <svg class="tip-icon" viewBox="0 0 48 48"><rect x="8" y="2" width="38" height="38" rx="10" fill="var(--lime)"/><path d="M4 32 L20 46 M20 32 L4 46" stroke="var(--alert)" stroke-width="5" stroke-linecap="square"/></svg>
      <p class="tip-title">NO SHARING</p><p class="tip-text">bring your own cup - don’t share cups and food</p>
    </li>
    <li class="tip">
      <svg class="tip-icon" viewBox="0 0 48 48"><rect x="8" y="2" width="38" height="38" rx="10" fill="var(--lime)"/><path d="M4 32 L20 46 M20 32 L4 46" stroke="var(--alert)" stroke-width="5" stroke-linecap="square"/></svg>
      <p class="tip-title">ELBOW TAP</p><p class="tip-text">instead of handshakes</p>
    </li>
    <li class="tip">
      <svg class="tip-icon" viewBox="0 0 48 48"><rect x="8" y="2" width="38" height="38" rx="10" fill="var(--lime)"/><path d="M3 46 L22 28" stroke="var(--alert)" stroke-width="5" stroke-linecap="round"/><path d="M3 40 L8 46" stroke="var(--alert)" stroke-width="5" stroke-linecap="round"/></svg>
      <p class="tip-title">WASH YOUR HANDS OFTEN</p><p class="tip-text">with soap for 20 seconds</p>
    </li>
    <li class="tip">
      <svg class="tip-icon" viewBox="0 0 48 48"><rect x="8" y="2" width="38" height="38" rx="10" fill="var(--lime)"/><path d="M4 32 L20 46 M20 32 L4 46" stroke="var(--alert)" stroke-width="5" stroke-linecap="square"/></svg>
      <p class="tip-title">USE YOUR ELBOW OR TISSUES</p><p class="tip-text">when you cough or sneeze and put tissues in the bin immediately</p>
    </li>
    <li class="tip">
      <svg class="tip-icon" viewBox="0 0 48 48"><rect x="8" y="2" width="38" height="38" rx="10" fill="var(--lime)"/><path d="M4 32 L20 46 M20 32 L4 46" stroke="var(--alert)" stroke-width="5" stroke-linecap="square"/></svg>
      <p class="tip-title">LEAVE YOUR FACE ALONE</p><p class="tip-text">after touching shared spaces</p>
    </li>
    <li class="tip">
      <svg class="tip-icon" viewBox="0 0 48 48"><path d="M26 2 L46 20 L40 20 L40 40 L12 40 L12 20 L6 20 Z" fill="var(--lime)"/><path d="M3 46 L22 28" stroke="var(--alert)" stroke-width="5" stroke-linecap="round"/><path d="M3 40 L8 46" stroke="var(--alert)" stroke-width="5" stroke-linecap="round"/></svg>
      <p class="tip-title">STAY AT HOME</p><p class="tip-text">if you’re feeling unwell</p>
    </li>
  </ul>

  <svg class="footer-shape" viewBox="0 0 720 1018" aria-hidden="true"><path d="M0 877 C110 830 200 818 278 818 C400 818 492 880 482 962 C479 988 470 1005 458 1018 L0 1018 Z" fill="var(--lime)"/></svg>

  <p class="helpline">0800 472 9160</p>
  <p class="helpline-note">Call Nurseline if you have a cough, a high temperature and shortness of breath.</p>
  <div class="partners"><span class="partner-circle"></span><span class="partner-square"></span></div>
  <p class="source">Based on recommendations from ZPK and QLN</p>

  <div class="brand"><span class="brand-dot"></span><span class="brand-name">Thrive<br>at Work</span></div>
</main>
</body>
</html>
```